sign business needs card design

I need a very clean design for my business card.
It is a sign company. Banners By Noon is the name of the business.
Our colors are orange, yellow. But I want a very professional card.
But you can use any colors. I like a black background with orange letters or a white back with a clean look. No cartoon or kiddy looking print. The info. I need on the card is as follows.
Banners By Noon
318.514.7702 ph.
318.514.7739 fax.
email.bannersbynoon@velmora.net
web.bannersbynooninc.example
4172 N. Calloway Ridge Ste. 2b
Dale Kessner

```html
<!DOCTYPE html>
<html lang="en">
<head>
<meta charset="utf-8">
<title>Banners By Noon – Business Card</title>
<link rel="stylesheet" href="https://fonts.googleapis.com/css2?family=Ubuntu:wght@400;500&display=swap">
<style>
  :root {
    --orange: #f26a2a;
    --green: #8cc63f;
    --red: #9e1a1e;
    --paper: #ffffff;
    --ghost: #fde9de;
    --icon: #8a8a8a;
  }
  html, body {
    margin: 0;
    padding: 0;
    overflow: hidden;
    background: var(--paper);
  }
  .card {
    position: relative;
    width: 1200px;
    height: 667px;
    overflow: hidden;
    background: var(--paper);
    font-family: "Ubuntu", sans-serif;
  }
  .card__bands {
    position: absolute;
    inset: 0;
    width: 1200px;
    height: 667px;
  }
  .band--line { fill: none; stroke: var(--green); stroke-width: 6; stroke-linecap: round; }
  .band--base { fill: var(--red); }

  .card__name {
    position: absolute;
    left: 113px;
    top: 44px;
    margin: 0;
    font-family: "Ubuntu", sans-serif;
    font-weight: 500;
    font-size: 80px;
    line-height: 1;
    color: var(--orange);
    letter-spacing: -1px;
  }
  .card__ghost-word {
    position: absolute;
    left: 56px;
    top: 290px;
    margin: 0;
    font-family: "Ubuntu", sans-serif;
    font-size: 112px;
    line-height: 1;
    letter-spacing: 12px;
    color: var(--ghost);
  }
  .contact {
    position: absolute;
    left: 642px;
    top: 0;
    margin: 0;
    padding: 0;
    list-style: none;
    color: var(--orange);
    font-size: 27px;
    line-height: 38px;
  }
  .contact__item {
    position: absolute;
    left: 0;
    display: flex;
    align-items: flex-start;
    gap: 22px;
  }
  .contact__item--address { top: 188px; }
  .contact__item--fax { top: 280px; }
  .contact__item--phone { top: 333px; }
  .contact__item--email { top: 379px; }
  .contact__item--web { top: 433px; }
  .contact__icon {
    flex: 0 0 34px;
    width: 34px;
    height: 38px;
  }
  .contact__text { white-space: nowrap; }
  .icon-stroke { fill: none; stroke: var(--icon); stroke-width: 2; }
  .icon-fill { fill: var(--icon); }
</style>
</head>
<body>
<main class="card">
  <svg class="card__bands" viewBox="0 0 1200 667" aria-hidden="true">
    <path class="band--line" d="M60,158 Q620,215 1200,92"/>
    <path class="band--base" d="M0,600 Q600,640 1200,548 L1200,667 L0,667Z"/>
    <path class="band--line" d="M0,560 Q600,612 1200,510"/>
  </svg>

  <h1 class="card__name">Banners By Noon</h1>
  <p class="card__ghost-word" aria-hidden="true">Banners</p>

  <ul class="contact">
    <li class="contact__item contact__item--address">
      <svg class="contact__icon" viewBox="0 0 34 38" aria-hidden="true">
        <path class="icon-fill" d="M17,2 C9,2 5,8 5,13 C5,20 14,26 17,37 C20,26 29,20 29,13 C29,8 25,2 17,2Z"/>
        <circle cx="17" cy="12" r="2.5" fill="#c0282d"/>
      </svg>
      <span class="contact__text">4172 N. Calloway Ridge Ste. 2b<br>Dale Kessner</span>
    </li>
    <li class="contact__item contact__item--fax">
      <svg class="contact__icon" viewBox="0 0 34 38" aria-hidden="true">
        <rect class="icon-stroke" x="3" y="16" width="28" height="14" rx="2"/>
        <rect class="icon-stroke" x="9" y="8" width="16" height="9"/>
        <line class="icon-stroke" x1="7" y1="24" x2="27" y2="24"/>
      </svg>
      <span class="contact__text">318.514.7739 fax.</span>
    </li>
    <li class="contact__item contact__item--phone">
      <svg class="contact__icon" viewBox="0 0 34 38" aria-hidden="true">
        <path class="icon-fill" d="M4,15 C4,9 30,9 30,15 L26,18 L22,15 L12,15 L8,18Z"/>
        <rect class="icon-fill" x="7" y="19" width="20" height="13" rx="3"/>
      </svg>
      <span class="contact__text">318.514.7702 ph.</span>
    </li>
    <li class="contact__item contact__item--email">
      <svg class="contact__icon" viewBox="0 0 34 38" aria-hidden="true">
        <circle class="icon-stroke" cx="17" cy="19" r="12"/>
        <circle class="icon-stroke" cx="17" cy="19" r="5"/>
        <path class="icon-stroke" d="M22,14 L22,22 C22,25 28,25 29,20"/>
      </svg>
      <span class="contact__text">email.bannersbynoon@velmora.net</span>
    </li>
    <li class="contact__item contact__item--web">
      <svg class="contact__icon" viewBox="0 0 34 38" aria-hidden="true">
        <circle class="icon-stroke" cx="17" cy="19" r="12"/>
        <ellipse class="icon-stroke" cx="17" cy="19" rx="5" ry="12"/>
        <line class="icon-stroke" x1="5" y1="19" x2="29" y2="19"/>
      </svg>
      <span class="contact__text">web.bannersbynooninc.example</span>
    </li>
  </ul>
</main>
</body>
</html>
```